Occupational Therapy Clinic Advertisement

Create an advertisement for a magazine. Below I have attached my original ad (Ad 2020.pdf) . I want the ad changed and it should be eye catching. I would like a eye catching graphics added in the ad. It should be a graphic image that applies to education. I am attaching a sample graphic image of that I liked from someone elses ad- it should not be the same- it just is there to show what I like. Please use the same words from my original ad.Dimensions: 3.75in x 10.3 in

Target Market(s)

Parents of School aged children

Requirements
Must have
• Must have eye catching Graphic. Colors should be eye catching for a typed magazine.

```html
<!DOCTYPE html>
<html lang="en">
<head>
<meta charset="utf-8">
<title>Bright Path OT Services – Magazine Ad</title>
<link rel="stylesheet" href="https://fonts.googleapis.com/css2?family=Arimo:wght@400;700&display=swap">
<style>
  :root {
    --brand-red: #a81f24;
    --ink: #111111;
    --paper: #ffffff;
    --backdrop: #e8e5e1;
    --bulb-yellow: #f3e04a;
    --bulb-shade: #d9c22c;
  }
  * { box-sizing: border-box; margin: 0; padding: 0; }
  html, body {
    width: 1200px; height: 1200px; overflow: hidden;
    background: var(--backdrop);
    font-family: "Arimo", Arial, sans-serif;
  }
  .ad {
    position: absolute; left: 396px; top: 40px;
    width: 408px; height: 1120px;
    background: var(--paper); color: var(--ink);
    box-shadow: 0 6px 24px rgba(0,0,0,.18);
    overflow: hidden;
  }
  .masthead {
    position: absolute; left: 0; top: 0; width: 100%; height: 140px;
    background: var(--brand-red); color: var(--paper);
    text-align: center; font-weight: 700;
    padding-top: 30px;
  }
  .masthead .clinic-name { font-size: 36px; line-height: 40px; letter-spacing: .5px; }
  .masthead .clinic-type { font-size: 20px; line-height: 24px; margin-top: 2px; }
  .masthead .clinic-phone { font-size: 20px; line-height: 24px; }

  .questions { position: absolute; left: 18px; top: 180px; width: 372px; list-style: none; }
  .question {
    display: flex; align-items: center; height: 62px;
  }
  .question svg { flex: 0 0 36px; width: 36px; height: 36px; }
  .question span {
    flex: 1; text-align: center; font-weight: 700; font-size: 15.5px;
    line-height: 19px; text-transform: uppercase; padding-left: 6px;
  }

  .headline {
    position: absolute; left: 0; top: 390px; width: 100%;
    text-align: center; font-weight: 700; font-size: 25px; line-height: 37px;
  }

  .idea-graphic {
    position: absolute; left: 100px; top: 470px; width: 220px; height: 190px;
    border-radius: 50% 50% 40% 40%;
    background: radial-gradient(circle at 50% 40%, var(--bulb-yellow) 0%, var(--bulb-shade) 55%, rgba(217,194,44,0) 75%);
  }

  .service-note {
    position: absolute; text-align: center; font-weight: 700;
    font-size: 17px; line-height: 21px;
  }
  .service-note.evaluate { left: 28px; top: 668px; width: 170px; }
  .service-note.deficits { left: 226px; top: 664px; width: 170px; }
  .service-note.treat { left: 30px; top: 762px; width: 170px; }

  .age-range {
    position: absolute; left: 0; top: 828px; width: 408px; padding-left: 6px;
    text-align: center; font-weight: 700; font-size: 30px;
  }

  .footer {
    position: absolute; left: 0; top: 878px; width: 100%; height: 242px;
    background: var(--brand-red); color: var(--paper);
    text-align: center; padding-top: 24px;
  }
  .footer .rsa { font-weight: 700; font-size: 20px; line-height: 26px; }
  .footer .location { font-weight: 700; font-size: 12.5px; line-height: 17px; margin-top: 6px; }
  .footer .contact-lead { font-weight: 700; font-size: 13px; line-height: 17px; margin-top: 14px; }
  .footer .contact-email { font-weight: 700; font-size: 17px; line-height: 22px; }
  .footer .therapist { font-weight: 700; font-size: 21px; line-height: 27px; margin-top: 16px; }
  .footer .therapist-phone { font-weight: 700; font-size: 21px; line-height: 27px; }
</style>
</head>
<body>
  <article class="ad">
    <header class="masthead">
      <div class="clinic-name">BRIGHT PATH</div>
      <div class="clinic-type">OT SERVICES</div>
      <div class="clinic-phone">(555) 014-2298</div>
    </header>

    <ul class="questions">
      <li class="question">
        <svg viewBox="0 0 36 36" aria-hidden="true"><circle cx="18" cy="18" r="18" fill="var(--brand-red)"/><g stroke="#fff" stroke-width="1.6" fill="#fff"><line x1="18" y1="18" x2="10" y2="11"/><line x1="18" y1="18" x2="26" y2="11"/><line x1="18" y1="18" x2="10" y2="25"/><line x1="18" y1="18" x2="26" y2="25"/><circle cx="18" cy="18" r="3.2"/><circle cx="10" cy="11" r="2.4"/><circle cx="26" cy="11" r="2.4"/><circle cx="10" cy="25" r="2.4"/><circle cx="26" cy="25" r="2.4"/></g></svg>
        <span>Does your child struggle<br>with reading/kriah?</span>
      </li>
      <li class="question">
        <svg viewBox="0 0 36 36" aria-hidden="true"><circle cx="18" cy="18" r="18" fill="var(--brand-red)"/><g stroke="#fff" stroke-width="1.6" fill="#fff"><line x1="18" y1="18" x2="10" y2="11"/><line x1="18" y1="18" x2="26" y2="11"/><line x1="18" y1="18" x2="10" y2="25"/><line x1="18" y1="18" x2="26" y2="25"/><circle cx="18" cy="18" r="3.2"/><circle cx="10" cy="11" r="2.4"/><circle cx="26" cy="11" r="2.4"/><circle cx="10" cy="25" r="2.4"/><circle cx="26" cy="25" r="2.4"/></g></svg>
        <span>Knows the information<br>but fails the test?</span>
      </li>
      <li class="question">
        <svg viewBox="0 0 36 36" aria-hidden="true"><circle cx="18" cy="18" r="18" fill="var(--brand-red)"/><g stroke="#fff" stroke-width="1.6" fill="#fff"><line x1="18" y1="18" x2="10" y2="11"/><line x1="18" y1="18" x2="26" y2="11"/><line x1="18" y1="18" x2="10" y2="25"/><line x1="18" y1="18" x2="26" y2="25"/><circle cx="18" cy="18" r="3.2"/><circle cx="10" cy="11" r="2.4"/><circle cx="26" cy="11" r="2.4"/><circle cx="10" cy="25" r="2.4"/><circle cx="26" cy="25" r="2.4"/></g></svg>
        <span>Has difficulty remembering<br>names and dates?</span>
      </li>
    </ul>

    <h1 class="headline">YES YOUR CHILD<br>WILL SUCCEED IN SCHOOL!</h1>

    <div class="idea-graphic" role="img" aria-label="Illustration of a crumpled yellow paper light bulb with hand-drawn rays and a trailing cord"></div>

    <p class="service-note evaluate">We Evaluate:<br>Using standardized<br>Evaluations</p>
    <p class="service-note deficits">We Treat the<br>underlying<br>processing deficits</p>
    <p class="service-note treat">We Treat:<br>Using Researched<br>based techniques</p>

    <p class="age-range">Ages: 6-18</p>

    <footer class="footer">
      <p class="rsa">Board of Ed OT RSA's accepted</p>
      <p class="location">Located in Borough Park<br>Evaluations done in Borough Park &amp; Staten Island</p>
      <p class="contact-lead">For more information or to be added to our email list,</p>
      <p class="contact-email">please email: brightpathot@example.com</p>
      <p class="therapist">Miriam Kessler OTR/L</p>
      <p class="therapist-phone">(555)014-2298</p>
    </footer>
  </article>
</body>
</html>
```